Quorvix Letter head

Quorvix is a young and energetic software development consultancy. We spend our time working with clients to turn what ever is in their heads in to software.
We are trying to create an image of a high class software boutique who build class leading bespoke solutions.
We need a sharp letter head that looks great on high quality media.
We like bold colours and distinctive design. So show us what you can do.
Industry/Entity Type
Software
Requirements
Must have
- Our company is based in the UK and are requried to have on the paper somewhere the following information:
* Registered company name: Quorvix Ltd
* Registered company number
* VAT registration number
In addition we also want the following:
* An email address
* Telephone number
* Website address
An example of what some pages have in their footer is something like the following:
Quorvix Ltd is registered in England and Wales. Reg. no: 5316274
Registered office: 48 Cobblewick Road, Harlow Essex, CM93TP. Tel: 07712365081
You do not have to use this sentance but please make sure your design incorporates accommodates the requirements for UK based companies

```html
<!DOCTYPE html>
<html lang="en">
<head>
<meta charset="utf-8">
<title>Quorvix Letterhead</title>
<link href="https://fonts.googleapis.com/css2?family=Raleway:wght@300;400;500&display=swap" rel="stylesheet">
<style>
  :root {
    --backdrop: #d8d8d8;
    --paper: #ffffff;
    --band: #c9c9c9;
    --ink: #8f8f8f;
    --ink-soft: #a8a8a8;
    --accent: #c8323c;
    --rule: #d4d4d4;
    --watermark: #ececec;
  }
  * { box-sizing: border-box; margin: 0; padding: 0; }
  html, body {
    width: 1200px; height: 968px; overflow: hidden;
    background: var(--backdrop);
    font-family: "Raleway", sans-serif;
  }
  .letterhead {
    position: absolute; left: 282px; top: 30px;
    width: 636px; height: 900px;
    background: var(--paper);
    box-shadow: 0 6px 18px rgba(0,0,0,0.12);
    overflow: hidden;
  }
  .watermark {
    position: absolute; left: 0; top: 0;
    width: 520px; height: 300px;
    background: linear-gradient(160deg, var(--watermark) 0%, #f3f3f3 55%, rgba(255,255,255,0) 100%);
    border-bottom-right-radius: 60px;
  }
  .footer {
    position: absolute; left: 30px; right: 28px; bottom: 44px;
    display: flex; align-items: flex-end; gap: 12px;
    color: var(--ink); font-size: 7.5px; line-height: 1.6; font-weight: 400;
    white-space: nowrap;
  }
  .footer > * { flex: none; }
  .footer__legal { padding-right: 12px; border-right: 1px solid var(--rule); }
  .footer__legal .label { color: var(--accent); }
  .footer__contacts {
    display: grid; grid-template-columns: auto auto; column-gap: 10px;
  }
  .contact { display: flex; align-items: center; gap: 4px; }
  .contact svg { width: 8px; height: 8px; flex: none; }
  .brand {
    margin-left: auto; display: flex; align-items: center; gap: 6px;
    color: var(--ink-soft); font-size: 26px; font-weight: 300;
    letter-spacing: 1px; line-height: 1;
  }
  .brand__mark { width: 9px; height: 9px; background: var(--accent); }
  .band {
    position: absolute; left: 0; right: 0; bottom: 0; height: 24px;
    background: var(--band);
  }
</style>
</head>
<body>
  <main class="letterhead">
    <div class="watermark" role="img" aria-label="Large faint brand decoration"></div>
    <footer class="footer">
      <div class="footer__legal">
        Quorvix Ltd is registered in England and Wales<br>
        <span class="label">Reg. No:</span> 5316274 · <span class="label">VAT:</span> GB999 9999 73
      </div>
      <div class="footer__address">
        48 Cobblewick Road<br>
        Harlow Essex, CM93TP
      </div>
      <div class="footer__contacts">
        <div class="contact">
          <svg viewBox="0 0 10 10" aria-hidden="true"><circle cx="5" cy="5" r="5" fill="#c8323c"/><path d="M3.2 2.6c.3-.3.7-.2.9.1l.5.8c.1.2 0 .5-.2.6l-.3.2c.3.6.7 1 1.3 1.3l.2-.3c.2-.2.4-.3.6-.2l.8.5c.3.2.3.6.1.9-.5.6-1.300.6-2 .1-.9-.6-1.6-1.300-2.1-2.2-.4-.6-.3-1.3.2-1.8z" fill="#fff"/></svg>
          +44 1279 640 118
        </div>
        <div class="contact">
          <svg viewBox="0 0 10 10" aria-hidden="true"><circle cx="5" cy="5" r="5" fill="#c8323c"/><rect x="2.4" y="3.2" width="5.2" height="3.6" fill="none" stroke="#fff" stroke-width=".8"/><path d="M2.6 3.4 5 5.2l2.4-1.8" fill="none" stroke="#fff" stroke-width=".8"/></svg>
          info@quorvix.com
        </div>
        <div class="contact">
          <svg viewBox="0 0 10 10" aria-hidden="true"><circle cx="5" cy="5" r="5" fill="#c8323c"/><rect x="2.6" y="2.8" width="4.8" height="4.4" rx=".4" fill="none" stroke="#fff" stroke-width=".8"/><rect x="3.6" y="4.2" width="2.8" height="1.6" fill="#fff"/></svg>
          +44 1279 640 119
        </div>
        <div class="contact">
          <svg viewBox="0 0 10 10" aria-hidden="true"><circle cx="5" cy="5" r="5" fill="#c8323c"/><circle cx="5" cy="5" r="2.6" fill="none" stroke="#fff" stroke-width=".8"/><path d="M2.4 5h5.2M5 2.4c-1.2 1.4-1.2 3.8 0 5.2M5 2.4c1.2 1.4 1.2 3.8 0 5.2" fill="none" stroke="#fff" stroke-width=".6"/></svg>
          www.quorvix.com
        </div>
      </div>
      <div class="brand">
        <span class="brand__mark"></span>
        <span class="brand__name">QUORVIX</span>
      </div>
    </footer>
    <div class="band"></div>
  </main>
</body>
</html>
```